Ridgeway Moss - Facebook Cover Photo & Photo Icon Design

We’re looking for a Facebook Cover Photo and Profile Icon design for Ridgeway Moss, a leading Residential Real Estate brand under Ridgeway Property Agents, based in Capalaba and Alexandra Hills, Queensland, Australia.

This design will represent my professional real estate profile and needs to be bold, clean, and on-brand.

Deliverables:

Facebook Cover Photo (820 x 312 px, optimized for mobile + desktop)

Facebook Profile Icon (1:1 ratio, minimum 320 x 320 px)

Design Guidelines:

1. Must Include:

The Ridgeway Moss logo (provided after project start)

Use of the Ridgeway Property Agents brand colour palette (will be supplied)

Clear connection to residential real estate

2. Optional but Preferred:

A local photo or skyline of Capalaba or Alexandra Hills in QLD (bonus points for this)

Space for a short tagline like:
“Selling Faster. Selling Smarter. Selling Ridgeway.”
(Optional tagline – open to variations if it improves layout/design)

3. Style & Feel:

Professional yet personable

Clean, modern aesthetic

Subtle touches of fun or personality are welcome

Layout must work well when overlaid by Facebook UI elements (like profile photo & call-to-action buttons)

Who I Am:
I'm a well-known residential real estate agent in the Redlands area, known for high-energy campaigns, premium video marketing, and a results-driven approach. My brand is fun, fresh, and high-performing — just like the real estate campaigns I run.

Files to be Provided (after selection):

Ridgeway Moss logo in high-res

Brand colour palette / style reference

Optional photo references if local imagery is not sourced by designer

Final Notes:

Make sure all text is legible on mobile and desktop

Original, layered design files must be delivered (PSD or AI preferred)

Bonus points if it feels uniquely “Bayside Queensland” while maintaining a national-level professional polish

Target Market(s)

Alexandra Hills, Capalaba & Sheldon

Industry/Entity Type

Real Estate

Colors
0054AA
0677BA
7BADD7
CADEEF
E8F1F8

Requirements
Must have
• Headshot, Mobile Number 0491 726 805, Suburbs - Alexandra Hills, Capalaba & Sheldon
Nice to have
• White, Crisp & Professional. Bottom Banner with Suburb List. Specialising in Alexandra Hills, Capalaba & Sheldon

```html
<!DOCTYPE html>
<html lang="en">
<head>
<meta charset="utf-8">
<title>Ridgeway Moss – Facebook Cover &amp; Profile Icon</title>
<link href="https://fonts.googleapis.com/css2?family=Poppins:wght@300;400;600;700&display=swap" rel="stylesheet">
<style>
  :root {
    --stage: #021559;
    --brand-blue: #0054AA;
    --mid-blue: #0677BA;
    --sky-blue: #7BADD7;
    --pale-blue: #CADEEF;
    --ice-blue: #E8F1F8;
    --ink: #0f1a3d;
    --paper: #ffffff;
    --mist: #eef3f8;
  }
  html, body {
    margin: 0;
    width: 1200px;
    height: 1000px;
    overflow: hidden;
    background: var(--stage);
    font-family: "Poppins", sans-serif;
  }
  .artboard {
    position: relative;
    width: 1200px;
    height: 1000px;
  }
  .cover {
    position: absolute;
    left: 50px;
    top: 70px;
    width: 1100px;
    height: 405px;
    display: block;
    border-radius: 10px;
    overflow: hidden;
  }
  .profile-icon {
    position: absolute;
    left: 450px;
    top: 560px;
    width: 300px;
    height: 300px;
    border-radius: 50%;
    background: var(--brand-blue);
    border: 6px solid var(--paper);
    box-sizing: border-box;
    display: flex;
    flex-direction: column;
    align-items: center;
    justify-content: center;
  }
  .profile-name {
    color: var(--paper);
    font-weight: 300;
    font-size: 34px;
    letter-spacing: 4px;
    line-height: 1.15;
    text-align: center;
    text-transform: uppercase;
  }
  .cover-text { font-family: "Poppins", sans-serif; }
  .tagline { font-weight: 700; font-size: 15.5px; fill: var(--ink); }
  .suburbs { font-weight: 600; font-size: 8.5px; fill: var(--mid-blue); letter-spacing: .6px; }
  .room-label { font-weight: 600; font-size: 7px; fill: var(--paper); letter-spacing: .5px; }
  .phone-number { font-weight: 700; font-size: 21px; fill: var(--ink); }
  .web-address { font-weight: 400; font-size: 7.5px; fill: var(--ink); letter-spacing: 1.5px; }
  .cta-label { font-weight: 600; font-size: 8px; fill: var(--brand-blue); }
</style>
</head>
<body>
<main class="artboard">

  <svg class="cover" viewBox="0 0 820 302" preserveAspectRatio="none" aria-label="Ridgeway Moss Facebook cover">
    <defs>
      <linearGradient id="landscape-tone" x1="0" y1="0" x2="0" y2="1">
        <stop offset="0" stop-color="#8fa4b4"/>
        <stop offset=".45" stop-color="#5d7268"/>
        <stop offset="1" stop-color="#3b4a3a"/>
      </linearGradient>
      <linearGradient id="agent-tone" x1="0" y1="0" x2="0" y2="1">
        <stop offset="0" stop-color="#c9a189"/>
        <stop offset=".35" stop-color="#e9e6e2"/>
        <stop offset="1" stop-color="#2e3b52"/>
      </linearGradient>
      <linearGradient id="room-tone" x1="0" y1="0" x2="1" y2="1">
        <stop offset="0" stop-color="#e8ded0"/>
        <stop offset="1" stop-color="#a9876a"/>
      </linearGradient>
    </defs>

    <!-- backdrop -->
    <rect class="backdrop" width="820" height="302" fill="var(--mist)"/>
    <polygon class="light-wedge" points="560,302 820,150 820,302" fill="var(--paper)"/>
    <polygon class="light-wedge" points="640,60 820,60 820,140 600,200" fill="var(--ice-blue)"/>

    <!-- landscape -->
    <g role="img" aria-label="Photo of green hills and valley under a soft sky">
      <polygon points="0,0 640,0 240,302 0,302" fill="url(#landscape-tone)"/>
    </g>

    <!-- corner accents -->
    <polygon class="accent-blue" points="615,0 800,0 705,42" fill="var(--mid-blue)"/>
    <polygon class="accent-pale" points="800,0 820,0 820,70 705,42" fill="var(--pale-blue)"/>
    <polygon class="accent-brand" points="598,302 775,222 820,240 820,302" fill="var(--brand-blue)"/>

    <!-- room photo strip -->
    <g class="room-strip" transform="translate(205,300) rotate(-30)">
      <g role="img" aria-label="Photo of a dining room">
        <rect x="0" y="-100" width="125" height="94" fill="url(#room-tone)" stroke="var(--paper)" stroke-width="4"/>
      </g>
      <rect x="20" y="-14" width="84" height="17" rx="8.5" fill="var(--mid-blue)"/>
      <text class="cover-text room-label" x="62" y="-3" text-anchor="middle">DINING ROOM</text>

      <g role="img" aria-label="Photo of a bedroom">
        <rect x="133" y="-100" width="125" height="94" fill="url(#room-tone)" stroke="var(--paper)" stroke-width="4"/>
      </g>
      <rect x="158" y="-14" width="74" height="17" rx="8.5" fill="var(--mid-blue)"/>
      <text class="cover-text room-label" x="195" y="-3" text-anchor="middle">BED ROOM</text>

      <g role="img" aria-label="Photo of a living room">
        <rect x="266" y="-100" width="125" height="94" fill="url(#room-tone)" stroke="var(--paper)" stroke-width="4"/>
      </g>
      <rect x="288" y="-14" width="80" height="17" rx="8.5" fill="var(--mid-blue)"/>
      <text class="cover-text room-label" x="328" y="-3" text-anchor="middle">LIVING ROOM</text>
    </g>

    <!-- agent headshot -->
    <g role="img" aria-label="Headshot of the agent in a navy suit and white shirt">
      <path d="M0,302 L0,90 Q0,40 60,40 L150,40 Q215,40 215,100 L215,302 Z" fill="url(#agent-tone)"/>
    </g>

    <!-- tagline -->
    <g class="tagline-block">
      <text class="cover-text tagline" x="782" y="158" text-anchor="end">SELLING FASTER</text>
      <circle cx="796" cy="153" r="3" fill="var(--mid-blue)"/>
      <text class="cover-text tagline" x="782" y="182" text-anchor="end">SELLING SMARTER</text>
      <circle cx="796" cy="177" r="3" fill="var(--mid-blue)"/>
      <text class="cover-text tagline" x="782" y="206" text-anchor="end">SELLING RIDGEWAY</text>
      <circle cx="796" cy="201" r="3" fill="var(--mid-blue)"/>
      <text class="cover-text suburbs" x="799" y="226" text-anchor="end">ALEXANDRA HILLS · CAPALABA · SHELDON</text>
    </g>

    <!-- contact -->
    <g class="contact-block">
      <g class="phone-icon" transform="translate(490,232)" fill="var(--mid-blue)">
        <path d="M1,5 Q10,-1 19,5 L17,9 L13,8 L13,6 Q10,5 7,6 L7,8 L3,9 Z"/>
        <rect x="4" y="9" width="12" height="9" rx="2"/>
      </g>
      <text class="cover-text phone-number" x="500" y="272" text-anchor="middle">0491 726 805</text>
      <text class="cover-text web-address" x="500" y="286" text-anchor="middle">WWW.RIDGEWAYMOSS.EXAMPLE</text>
    </g>

    <!-- call to action -->
    <rect class="cta-button" x="705" y="267" width="90" height="24" rx="12" fill="var(--pale-blue)"/>
    <text class="cover-text cta-label" x="750" y="282" text-anchor="middle">BOOK NOW</text>
  </svg>

  <div class="profile-icon">
    <span class="profile-name">Ridgeway</span>
    <span class="profile-name">Moss</span>
  </div>

</main>
</body>
</html>
```